Advanced training flyer for defence industry - professional

U.S. Export Controls are some of the most complex and stringent in the world. The U.S. Government regulates the transfer of U.S. origin goods and technical data throughout the world, with the intent of preventing unauthorised transfer of technology and know-how.

These controls extend world-wide and can impact anyone dealing in U.S. controlled goods or technology.

This three-day advanced course is designed to give attendees a greater understanding of U.S. Export Controls from a non-U.S. perspective in practical and relevant terms. Though we will cover a lot of material the course is designed for practitioner with an existing knowledge.

We need a flyer design for an advanced course for the previously mentioned content.

Please include text boxes in order for the form to be completed online.

defence industry

Training

• Please include text boxes so that the form can be completed online.
• flags incorporated

```html
<!DOCTYPE html>
<html lang="en">
<head>
<meta charset="utf-8">
<title>Advanced Defence, EAR &amp; ITAR Training – Flyer</title>
<link href="https://fonts.googleapis.com/css2?family=Jost:ital,wght@0,400;0,500;0,700;0,800;1,400;1,500;1,700&display=swap" rel="stylesheet">
<style>
:root{
  --stage:#7a1416;
  --navy:#2e3192;
  --red:#e21d25;
  --green:#1d8a3b;
  --ink:#1b1b1f;
  --paper:#f4f5f9;
  --rule:#5a5a66;
}
*{box-sizing:border-box;margin:0;padding:0}
html,body{width:844px;height:1200px;overflow:hidden}
body{background:var(--stage);font-family:'Jost',sans-serif;color:var(--ink);position:relative}

.sheet{position:absolute;left:60px;width:738px;height:521px;background:var(--paper);box-shadow:0 3px 10px rgba(0,0,0,.45);overflow:hidden}
.sheet--outer{top:44px}
.sheet--inner{top:618px}
.flag-wash{position:absolute;inset:0;
  background:
   linear-gradient(155deg,rgba(255,255,255,.0) 0%,rgba(214,50,62,.16) 22%,rgba(255,255,255,.55) 38%,rgba(40,62,150,.20) 58%,rgba(255,255,255,.5) 72%,rgba(214,50,62,.14) 90%),
   linear-gradient(90deg,#e6e9f3,#f7f7fa 55%,#e9ecf5)}

.col{position:absolute;top:0;height:100%;overflow:hidden}

/* ---------- outer sheet ---------- */
.bar{background:var(--navy);color:#fff;font-weight:700;font-style:italic;font-size:10.5px;letter-spacing:.3px;height:21px;line-height:21px;padding-left:14px}
.registration{left:0;width:242px}
.payment{left:242px;width:249px;border-left:1px solid rgba(255,255,255,.6)}
.cover{left:491px;width:247px;background:rgba(255,255,255,.72)}

.form{padding:12px 10px 0 10px}
.form-row{display:flex;align-items:flex-end;font-size:12.5px;line-height:16.5px;height:16.5px;min-width:0}
.form-row label{white-space:nowrap;margin-right:2px;flex:none}
.field{flex:1 1 0;width:0;min-width:0;border:0;border-bottom:1px dotted var(--rule);background:transparent;font:inherit;font-size:11px;height:12px;outline:none}
.gap{height:12px}
.form-row--tall{height:19px}

.fee-bar{margin-top:14px}
.fee-row{display:flex;align-items:center;border-bottom:1px solid rgba(0,0,0,.15);padding:0 10px 0 14px;font-size:8.5px;font-style:italic}
.fee-row strong{font-size:10px;font-weight:700}
.fee-row .fee-name{flex:1;line-height:1.25}
.fee-row .price{width:40px;font-style:normal;font-size:9px}
.tick{appearance:none;-webkit-appearance:none;width:12px;height:12px;border:1px solid #333;background:#fff;margin-right:10px;flex:none;vertical-align:middle}
.tick--sm{width:10px;height:10px;margin:0 3px 0 4px}

.pay{padding:6px 8px 0 8px}
.pay-line{font-size:12px;line-height:16px;display:flex;align-items:center;white-space:nowrap}
.pay-line .tick{margin:0 2px 0 4px}
.pay-card{padding-left:20px}
.pay-card .form-row{font-size:12px;height:16px;line-height:16px}
.pay-rule{border-bottom:1px dotted var(--rule);margin:6px 0 4px}
.note{font-size:6.8px;font-style:italic;line-height:1.3;padding-left:6px}

.box{border:1.2px solid #222;border-radius:8px;background:rgba(255,255,255,.82);position:relative;margin:0 8px}
.box-tab{position:absolute;left:50%;top:-9px;transform:translateX(-50%);background:var(--navy);color:#fff;font-weight:700;font-style:italic;font-size:11px;padding:1px 12px;border-radius:3px;border:1.5px solid #fff;outline:1px solid var(--navy)}
.venue{margin-top:17px;height:78px;text-align:center;padding-top:9px;font-size:9px;line-height:1.35}
.venue strong{font-style:italic;font-size:10px}
.policies{margin-top:17px;height:202px;padding:10px 8px 0 8px;font-size:7px;line-height:1.3}
.policies p{margin-bottom:6px}
.policies ul{list-style:none;padding-left:60px}
.policies li::before{content:"• "}
.contact-foot{position:absolute;left:0;right:0;bottom:0;height:25px;background:var(--navy);border-radius:14px 14px 0 0;color:#fff;text-align:center;font-style:italic;font-size:8px;line-height:1.25;padding-top:3px}

.brand{display:flex;align-items:center;justify-content:center;gap:8px;margin:18px 0 0}
.brand-dot{width:42px;height:42px;border-radius:50%;background:var(--green);flex:none}
.brand-name{font-size:15px;font-weight:500;color:var(--green);line-height:1.05;width:150px}
.title{text-align:center;color:var(--navy);font-weight:800;font-size:28px;margin-top:22px;line-height:1}
.subtitle{text-align:center;color:var(--red);font-size:10.5px;font-weight:500;margin-top:2px}
.course-card{margin:6px 14px 0;border:1.5px dashed var(--navy);border-radius:8px;padding:3px}
.course-card .inner{background:var(--navy);border-radius:6px;color:#fff;text-align:center;font-weight:700;overflow:hidden}
.course-card .head{background:var(--red);margin:0 30px;border-radius:0 0 6px 6px;font-size:11.5px;padding:2px 0}
.course-card .dates{font-size:10.5px;line-height:1.35;padding:3px 0 4px}
.course-card .hours{background:var(--red);font-size:10.5px;padding:3px 0}
.blurb{padding:12px 12px 0;font-size:7px;line-height:1.3}
.blurb p{margin-bottom:7px}
.blurb b{color:var(--green)}
.offer{display:flex;align-items:center;gap:8px;padding:3px 12px 0}
.price-badge{width:58px;height:30px;background:var(--navy);border:2px solid #fff;outline:1px solid var(--navy);border-radius:8px;color:#fff;text-align:center;font-weight:700;font-size:10px;line-height:1.05;padding-top:2px;position:relative}
.price-badge span{display:block;font-size:5.5px;font-weight:500;color:#ffd0d2}
.guest{flex:1;border:1px solid var(--navy);border-radius:6px;font-size:6px;font-style:italic;padding:3px 5px;line-height:1.3;background:#fff}
.audience-bar{background:var(--navy);color:#fff;text-align:center;font-weight:700;font-size:12px;height:20px;line-height:20px;margin-top:12px}
.audience{font-size:7px;line-height:1.3;padding:4px 12px}

/* ---------- inner sheet ---------- */
.day{width:246px;padding:0}
.day--1{left:0}.day--2{left:246px}.day--3{left:492px}
.day-bar{background:var(--navy);color:#fff;text-align:center;font-weight:700;font-size:12.5px;height:29px;line-height:29px}
.day-title{text-align:center;font-style:italic;font-weight:700;font-size:13px;margin-top:8px;line-height:1.1}
.day-title span{display:block;font-weight:400;font-size:14px}
.day-body{padding:8px 8px 0 30px;font-style:italic}
.day-body h3{font-size:10.5px;font-weight:700;margin-top:9px;line-height:1.15}
.day-body h4{font-size:9px;font-weight:400;line-height:1.2}
.day-body ul{list-style:none;font-size:8.8px;line-height:1.3;padding-left:0}
.day-body ul li::before{content:"• "}
.day-body ul.sub{font-size:6.8px;line-height:1.25;padding-left:22px}
.day-body ul.sub li::before{content:"o "}
.day-body p{font-size:8.8px;margin-top:10px}
.day--3 .day-body{padding-left:22px}
.day--3 .day-body ul{line-height:1.42}
.day--3 .day-body h3{margin-top:11px}
.day--3 .day-title{text-align:left;padding-left:22px;font-size:12.5px}
</style>
</head>
<body>

<section class="sheet sheet--outer">
  <div class="flag-wash" role="img" aria-label="Soft waving Australian and United States flags in red, white and blue behind the content"></div>

  <div class="col registration">
    <div class="bar">SEMINAR REGISTRATION</div>
    <div class="form">
      <div class="form-row"><label>Attendee 1 Name:</label><input class="field" type="text"></div>
      <div class="form-row"><label>email:</label><input class="field" type="email"></div>
      <div class="form-row"><label>Attendee 2 Name:</label><input class="field" type="text"></div>
      <div class="form-row"><label>email:</label><input class="field" type="email"></div>
      <div class="form-row"><label>Attendee 3 Name:</label><input class="field" type="text"></div>
      <div class="form-row"><label>email:</label><input class="field" type="email"></div>
      <div class="form-row"><label>Attendee 4 Name:</label><input class="field" type="text"></div>
      <div class="form-row"><label>email:</label><input class="field" type="email"></div>
      <div class="gap"></div>
      <div class="form-row form-row--tall"><label>Company:</label><input class="field" type="text"></div>
      <div class="form-row"><label style="visibility:hidden">Company:</label><input class="field" type="text"></div>
      <div class="form-row form-row--tall"><label>Address:</label><input class="field" type="text"></div>
      <div class="form-row"><label>City:</label><input class="field" type="text"></div>
      <div class="form-row"><label>Postcode:</label><input class="field" type="text"></div>
      <div class="form-row"><label>Phone:</label><input class="field" type="tel"></div>
      <div class="form-row"><label>Mobile no:</label><input class="field" type="tel"></div>
    </div>
    <div class="bar fee-bar" style="height:27px;line-height:27px">FEE</div>
    <div class="fee-row" style="height:48px"><div class="fee-name"><strong>Defence &amp; ITAR Training</strong><br>7 &amp; 8 September – Melbourne<br>21 &amp; 22 September - Sydney</div><input class="tick" type="checkbox"><span class="price">$1395</span></div>
    <div class="fee-row" style="height:52px"><div class="fee-name"><strong>ADVANCED Defence<br>&amp; ITAR Training</strong><br>9, 10, 11 September – Melbourne<br>23, 24, 25 September - Sydney</div><input class="tick" type="checkbox"><span class="price">$2295</span></div>
    <div class="fee-row" style="height:30px"><div class="fee-name">Or register for <strong>BOTH</strong> sessions</div><input class="tick" type="checkbox"><span class="price">$3295</span></div>
    <div class="fee-row" style="height:26px;border:0"><div class="fee-name" style="font-size:7.5px">Additional copies of workbook</div><input class="tick" type="checkbox"><span class="price">$ 99</span></div>
  </div>

  <div class="col payment">
    <div class="bar">PAYMENT</div>
    <div class="pay">
      <div class="pay-line">Payment method: <input class="tick tick--sm" type="checkbox">Invoice <input class="tick tick--sm" type="checkbox">Creadit Card</div>
      <div class="pay-line">Card type: <input class="tick tick--sm" type="checkbox">NovaCard <input class="tick tick--sm" type="checkbox">Veyra <input class="tick tick--sm" type="checkbox">Amplex</div>
      <div class="pay-card" style="margin-top:3px">
        <div class="form-row"><label>Card name:</label><input class="field" type="text"></div>
        <div class="form-row"><label>Card number:</label><input class="field" type="text"></div>
        <div class="form-row"><label>Expiry date:</label><input class="field" type="text" style="flex:1.6 1 0"><label style="margin-left:4px">CVV:</label><input class="field" type="text"></div>
        <div class="form-row"><label>Cardholder email:</label><input class="field" type="email"></div>
      </div>
      <div class="pay-rule"></div>
      <p class="note">Note: Credit card payments incur a 3% surcharge.<br>Amplex incurs 4%.</p>
    </div>

    <div class="box venue">
      <span class="box-tab">Venue</span>
      <strong>Harbourview Grand Hotel</strong><br>Harbour Street, Sydney<br><br>
      <strong>Riverside Plaza Melbourne</strong><br>Riverbank St, Melbourne
    </div>

    <div class="box policies">
      <span class="box-tab">POLICIES</span>
      <p>Cancellation<br>Cancellations incur a 20% administration fee.<br>No cancellations permitted within 30 days of training commencing.<br>If a registered attendee is unable to attend, a replacement attendee is allowed.</p>
      <p>Workbook<br>Each attendee will receive a workbook. The workbook is licenced for the use of the training attendee only. If you need other copies , please order them directly.</p>
      <p style="margin-bottom:2px">Multiple attendees<br>Attendees from the same company booked and paid for at the same time for the same course will received the below discounts:</p>
      <ul>
        <li><b>5 attendees</b><br>&nbsp;&nbsp;50% discount on the 6th attendee.</li>
        <li><b>10 attendees</b><br>&nbsp;&nbsp;11th attendee free</li>
        <li><b>&lt; 10 attendees</b> – contact us</li>
      </ul>
    </div>

    <div class="contact-foot">Email registrations to info@meridiantci.com<br>Fax to +61 (0)7 5555 0142</div>
  </div>

  <div class="col cover">
    <div class="brand"><span class="brand-dot"></span><span class="brand-name">Meridian Trade Compliance Institute</span></div>
    <h1 class="title">ADVANCED</h1>
    <p class="subtitle">DEFENCE, EAR &amp; ITAR Training</p>
    <div class="course-card"><div class="inner">
      <div class="head">3-DAY COURSE</div>
      <div class="dates">9, 10, 11 September – Melbourne<br>21, 22, 23 September – Sydney</div>
      <div class="hours">Program: 0900 to 1630 each day</div>
    </div></div>
    <div class="blurb">
      <p><b>U.S. Export Controls</b> are some of the most complex and stringent in the world. The U.S. Government regulates the transfer of U.S. origin goods and technical data throughout the world, with the intent of preventing unauthorised transfer of technology and know-how.</p>
      <p>These controls extend world-wide and can impact anyone dealing in U.S. controlled goods or technology.</p>
      <p><b>This three-day advanced course</b> is designed to give attendees a greater understanding of U.S. Export Controls from a non-U.S. perspective in practical and relevant terms. Though we will cover a lot of material the course is designed for practitioner with an existing knowledge</p>
    </div>
    <div class="offer">
      <div class="price-badge">$2295.00<span>AUD per person inc GST</span></div>
      <div class="guest">Guest presenters will deliver different aspects of the training program.</div>
    </div>
    <div class="audience-bar">WHO SHOULD ATTEND</div>
    <p class="audience">Practitioners that work for companies that deal with U.S. based technology or that purchase U.S origin products, components or technology. The Advanced course assumes a basic understand of U.S. trade controls.</p>
  </div>
</section>

<section class="sheet sheet--inner">
  <div class="flag-wash" role="img" aria-label="Soft waving Australian and United States flags in red, white and blue behind the program"></div>

  <div class="col day day--1">
    <div class="day-bar">DAY 1</div>
    <h2 class="day-title">EAR<span>Introduction</span></h2>
    <div class="day-body">
      <ul><li>Key concepts</li><li>Export Administration Regulations</li><li>Bureau of Industry &amp; Security</li></ul>
      <h3>How To Classify Your Item</h3>
      <ul><li>How to determine the Export Control<br>&nbsp;&nbsp;Classification Number</li></ul>
      <h3>Technology Controls</h3>
      <ul><li>What technology is subject to EAR;</li><li>License exceptions</li><li>Foreign items incorporating controlled<br>U.S.-origin technology</li><li>Encryption under the EAR</li></ul>
      <h3>Technical data Considerations</h3>
      <ul><li>Controls on physical and intangible data</li><li>Deemed export and re-exports</li><li>Third country national issues</li></ul>
      <h3>EAR Exceptions</h3>
      <ul><li>Terms, provisions, applicability and use<br>of Licence Exceptions</li><li>Changes to Exceptions</li><li>Restrictions governing the use of Exceptions</li><li>Distinction between list based and transaction<br>based Licence Exceptions</li></ul>
      <h3>Deemed Export</h3>
      <ul><li>How to determine when deemed<br>&nbsp;&nbsp;export licenses are necessary</li></ul>
      <h3>Export Control Reform</h3>
      <ul><li>ITAR to EAR</li><li>600 series</li><li>Specially designed</li><li>Handling licenses and approvals</li></ul>
    </div>
  </div>

  <div class="col day day--2">
    <div class="day-bar">DAY 2</div>
    <h2 class="day-title">ITAR<span>Introduction</span></h2>
    <div class="day-body">
      <ul><li>Key concepts</li><li>International Traffic in Arms Regulations</li></ul>
      <p>Understanding ITAR classifications</p>
      <p>How to classify an item in the ITAR</p>
      <h3>Re-exports &amp; re-transfers</h3>
      <ul><li>Licence free activity</li><li>Returning items to the U.S.</li></ul>
      <h3>ITAR approvals</h3>
      <ul><li>Licences</li><li>Agreements</li></ul>
      <ul class="sub"><li>Types of agreements</li><li>Sub-licensing</li><li>Dual nationals</li><li>NDA's</li><li>Amendments</li></ul>
      <h3>Brokering</h3>
      <ul><li>Extra-territorial application</li><li>Registration</li><li>Reporting requirements</li></ul>
      <p>Destruction and Disposal of ITAR items</p>
      <p>Defence services involving ITAR<br>controlled articles and technical data</p>
      <p>Recordkeeping for the ITAR</p>
      <h3>Foreign Military Sales</h3>
      <ul><li>Letter of Offer</li><li>Third Party Re-transfer Approvals</li><li>Export Control Reform and FMS</li></ul>
      <h3>Export Control Reform</h3>
      <ul><li>The ITAR definition of Specially Designed</li></ul>
    </div>
  </div>

  <div class="col day day--3">
    <div class="day-bar">DAY 3</div>
    <h2 class="day-title">COMPLIANCE &amp; ENFORCEMENT</h2>
    <div class="day-body">
      <h3>Trade Control Compliance Framework</h3>
      <ul><li>Document development</li><li>Infrastructure</li><li>Risk assessments</li><li>Internal self assessments</li></ul>
      <h3>Enforcement</h3>
      <ul><li>U.S. enforcement</li><li>Fines and penalties</li><li>Case studies</li><li>Preventing violations</li></ul>
      <h3>NON-US ISSUES</h3>
      <h4>Dual Nationals</h4>
      <ul><li>Anti-discrimination</li><li>Privacy</li></ul>
      <h3>AUSTRALIAN REGULATIONS</h3>
      <ul><li>Australia's System of Export Controls</li><li>Defence and Strategic Goods List?</li><li>Dual-Use List</li><li>Customs Act 1901</li><li>Defence Trade Controls Act 2012</li><li>Catch-All Legislation</li><li>Sanctions Legislation</li><li>Compliance philosophy</li><li>Non-compliance and penalties</li><li>Risk of diversion</li><li>Cyber security</li><li>Red flags</li><li>Self-Assessment Tool</li><li>AU-US Trade Co-operation Treaty</li><li>Managing the transition to intangibles</li></ul>
    </div>
  </div>
</section>

</body>
</html>
```